Biz cards

Need some business cards to handout when finding clients for medical marijuana

Industry/Entity Type

Business

Contact Information for Business Card

Name: Tobin Velk
Cell #555-314-2297
Instagram: lunarharvestco

Requirements
Must have
• Needs to say ( on back of card with my info )
• MMAR Producer
• Marijuana Enthusiest and connoisseur

```html
<!DOCTYPE html>
<html lang="en">
<head>
<meta charset="utf-8">
<title>Lunar Harvest – Business Cards</title>
<link rel="stylesheet" href="https://fonts.googleapis.com/css2?family=Montserrat:wght@400;800&family=Lato:wght@400&display=swap">
<style>
  :root {
    --page-bg: #e6e6e6;
    --card-bg: #ffffff;
    --ink: #1a1a1a;
    --brand-red: #e3262b;
    --faint-red: #fbeae6;
    --card-shadow: 0 10px 28px rgba(0,0,0,0.18);
  }
  * { box-sizing: border-box; margin: 0; padding: 0; }
  html, body { width: 1200px; height: 880px; overflow: hidden; }
  body {
    background: var(--page-bg);
    font-family: "Lato", sans-serif;
    color: var(--ink);
    position: relative;
  }
  .card {
    position: absolute;
    width: 560px;
    height: 320px;
    background: var(--card-bg);
    border-radius: 22px;
    box-shadow: var(--card-shadow);
    overflow: hidden;
  }
  .card--front { left: 90px; top: 90px; }
  .card--back { left: 550px; top: 470px; }

  /* Front */
  .brand {
    position: absolute;
    left: 0; right: 0; top: 96px;
    display: flex; align-items: center; justify-content: center; gap: 14px;
  }
  .brand__dot {
    width: 34px; height: 34px; border-radius: 50%;
    background: var(--brand-red);
  }
  .brand__name {
    font-family: "Montserrat", sans-serif;
    font-weight: 800;
    font-size: 40px;
    letter-spacing: -0.5px;
    text-transform: uppercase;
    color: var(--ink);
  }
  .tagline {
    position: absolute;
    left: 0; right: 0; top: 206px;
    text-align: center;
    font-size: 17px;
    color: var(--ink);
  }

  /* Back */
  .decor {
    position: absolute;
    right: -40px; top: -10px;
    width: 330px; height: 330px;
    border-radius: 50%;
    background: var(--faint-red);
  }
  .holder {
    position: absolute;
    left: 48px; top: 118px;
  }
  .holder__name {
    font-family: "Montserrat", sans-serif;
    font-weight: 800;
    font-size: 27px;
    text-transform: uppercase;
    line-height: 1;
  }
  .holder__role {
    font-size: 18px;
    color: var(--brand-red);
    margin-top: 4px;
  }
  .contacts {
    position: absolute;
    left: 60px; top: 206px;
    list-style: none;
  }
  .contacts__item {
    display: flex; align-items: center; gap: 10px;
    font-size: 18px;
    margin-bottom: 8px;
  }
  .contacts__icon { width: 24px; height: 24px; flex: none; }
</style>
</head>
<body>
  <section class="card card--front" aria-label="Card front">
    <div class="brand">
      <span class="brand__dot"></span>
      <span class="brand__name">Lunar Harvest</span>
    </div>
    <p class="tagline">Marijuana Enthusiest and Connoisseur</p>
  </section>

  <section class="card card--back" aria-label="Card back">
    <div class="decor" aria-hidden="true"></div>
    <div class="holder">
      <h1 class="holder__name">Tobin Velk</h1>
      <p class="holder__role">MMAR Producer</p>
    </div>
    <ul class="contacts">
      <li class="contacts__item">
        <svg class="contacts__icon" viewBox="0 0 24 24" aria-hidden="true">
          <circle cx="12" cy="12" r="10.5" fill="none" stroke="#e3262b" stroke-width="1.6"/>
          <rect x="8.5" y="6" width="7" height="12" rx="1.2" fill="none" stroke="#e3262b" stroke-width="1.5"/>
          <line x1="11" y1="15.8" x2="13" y2="15.8" stroke="#e3262b" stroke-width="1.4"/>
        </svg>
        <span>555-314-2297</span>
      </li>
      <li class="contacts__item">
        <svg class="contacts__icon" viewBox="0 0 24 24" aria-hidden="true">
          <circle cx="12" cy="12" r="10.5" fill="none" stroke="#e3262b" stroke-width="1.6"/>
          <circle cx="12" cy="12" r="4" fill="#e3262b"/>
        </svg>
        <span>lunarharvestco</span>
      </li>
    </ul>
  </section>
</body>
</html>
```